8.5 x 8.5 - HELOC Product Campaign

Home Equity Lines of Credit
are BACK!!!

* Up to 97.5% on Owner Occupied Properties
* 700 Minimum Scores
* Fund in only 2-3 weeks

Can be used for...
* Education Expense
* Bill Consolidation
* Home Improvement
* Investments

Call today for more information!
(800) 417-2960

Bluegate Lending Partners, Inc.
NMLS #381760
www.bluegatelendhub.com

```html
<!DOCTYPE html>
<html lang="en">
<head>
<meta charset="utf-8">
<title>Bluegate Lending Partners – HELOC Campaign</title>
<link rel="stylesheet" href="https://fonts.googleapis.com/css2?family=Barlow+Condensed:wght@500;600;700&family=Open+Sans:ital,wght@0,400;0,600;1,700&display=swap">
<style>
  :root{
    --stage:#4a4949;
    --paper:#ffffff;
    --gold:#a69a1e;
    --blue:#1d4f9f;
    --blue-deep:#0c2a62;
    --ink:#1f1f1f;
    --charcoal:#3b3b3b;
    --rule:#3f6fc0;
  }
  *{margin:0;padding:0;box-sizing:border-box}
  html,body{width:1200px;height:1000px;overflow:hidden;background:var(--stage)}
  .flyer{position:absolute;left:223px;top:108px;width:753px;height:753px;background:var(--paper);overflow:hidden;
    box-shadow:0 18px 24px rgba(0,0,0,.35)}
  .shapes{position:absolute;inset:0}
  .photo-top{position:absolute;left:250px;top:0;width:503px;height:265px;
    background:linear-gradient(90deg,rgba(255,255,255,1) 0%,rgba(214,208,200,.6) 22%,#b9b2a8 50%,#8a8580 80%,#c9c6c2 100%)}
  .brand{position:absolute;left:42px;top:60px;width:245px;display:flex;align-items:center;gap:12px}
  .brand-mark{width:34px;height:34px;background:var(--blue);flex:none}
  .brand-name{font-family:'Barlow Condensed',sans-serif;font-weight:600;font-size:27px;line-height:1.05;color:var(--blue)}
  .headline{position:absolute;left:48px;top:244px;font-family:'Barlow Condensed',sans-serif;font-weight:700;line-height:.98}
  .headline .lead{display:block;color:var(--gold);font-size:42px;letter-spacing:.3px}
  .headline .punch{display:block;color:var(--blue);font-size:60px;letter-spacing:.5px}
  .head-rule{position:absolute;left:48px;top:391px;width:206px;height:3px;background:var(--blue)}
  .ltv{position:absolute;left:47px;top:414px;display:flex;align-items:center;gap:16px}
  .ltv-figure{font-family:'Barlow Condensed',sans-serif;font-weight:700;font-size:36px;color:var(--gold)}
  .ltv-note{font-family:'Open Sans',sans-serif;font-size:18px;line-height:1.2;color:var(--ink)}
  .tag{position:absolute;font-family:'Open Sans',sans-serif;font-style:italic;font-weight:700;font-size:23px;color:#fff;letter-spacing:.3px}
  .tag-score{left:67px;top:468px}
  .tag-fund{left:93px;top:502px}
  .uses{position:absolute;left:47px;top:551px;width:410px}
  .uses h2{font-family:'Barlow Condensed',sans-serif;font-weight:600;font-size:30px;color:#fff;letter-spacing:.3px}
  .uses-rule{height:3px;background:var(--rule);margin-top:8px;opacity:.8}
  .uses ul{list-style:none;display:grid;grid-template-columns:205px 205px;row-gap:10px;margin-top:12px}
  .uses li{font-family:'Open Sans',sans-serif;font-size:17px;color:#fff;display:flex;align-items:center;gap:9px}
  .uses li svg{flex:none}
  .phone{position:absolute;left:46px;top:694px;display:flex;align-items:center;gap:12px;
    font-family:'Barlow Condensed',sans-serif;font-weight:700;font-size:46px;color:#fff}
  .contact{position:absolute;right:46px;top:670px;text-align:right;font-family:'Barlow Condensed',sans-serif;font-weight:500;font-style:normal;color:var(--ink)}
  .contact p{font-size:19px;line-height:25px}
  .contact .web{font-weight:600;font-size:26px;color:var(--gold);line-height:30px}
</style>
</head>
<body>
<main class="flyer">
  <div class="photo-top" role="img" aria-label="Photo of a worried couple sitting on a sofa reviewing bills"></div>

  <svg class="shapes" width="753" height="753" viewBox="0 0 753 753" aria-hidden="true">
    <defs>
      <linearGradient id="panelBlue" x1="0" y1="0" x2="0" y2="1">
        <stop offset="0" stop-color="#1d4f9f"/>
        <stop offset="1" stop-color="#0c2a62"/>
      </linearGradient>
      <linearGradient id="coupleTones" x1="0" y1="0" x2="1" y2="1">
        <stop offset="0" stop-color="#e6ddd3"/>
        <stop offset=".5" stop-color="#b9a596"/>
        <stop offset="1" stop-color="#6f7d8e"/>
      </linearGradient>
      <linearGradient id="gradTones" x1="0" y1="0" x2="0" y2="1">
        <stop offset="0" stop-color="#c9c2b4"/>
        <stop offset="1" stop-color="#1c2233"/>
      </linearGradient>
    </defs>
    <!-- white sweep with blue edge -->
    <path d="M0,265 Q160,205 360,222 L360,240 Q160,230 0,285 Z" fill="#fff"/>
    <path d="M0,268 Q160,208 350,222" fill="none" stroke="var(--blue)" stroke-width="7"/>
    <path d="M745,150 Q752,210 735,262" fill="none" stroke="var(--blue)" stroke-width="10"/>
    <!-- blue panel -->
    <path d="M0,478 C120,450 260,470 600,420 L600,700 L0,700 Z" fill="url(#panelBlue)"/>
    <path d="M0,470 C100,445 220,462 320,455" fill="none" stroke="#fff" stroke-width="14"/>
    <!-- banners -->
    <polygon points="50,466 372,466 362,499 44,499" fill="var(--charcoal)"/>
    <polygon points="80,499 428,499 418,534 72,534" fill="var(--gold)"/>
    <!-- gold footer -->
    <path d="M0,687 L470,687 Q440,718 420,753 L0,753 Z" fill="var(--gold)"/>
    <!-- gold sweep and white contact corner -->
    <path d="M395,753 C415,640 540,595 753,578 L753,605 C560,610 445,640 425,753 Z" fill="var(--gold)"/>
    <path d="M753,605 C560,610 445,640 425,753 L753,753 Z" fill="#fff"/>
    <!-- large circle -->
    <circle cx="612" cy="430" r="172" fill="var(--gold)"/>
    <circle cx="612" cy="430" r="163" fill="url(#coupleTones)" role="img" aria-label="Photo of a smiling couple looking at a tablet on a sofa"/>
    <!-- small circle -->
    <circle cx="400" cy="293" r="68" fill="var(--gold)"/>
    <circle cx="400" cy="293" r="62" fill="url(#gradTones)" role="img" aria-label="Photo of a smiling graduate in cap and gown holding a diploma"/>
  </svg>

  <div class="brand">
    <span class="brand-mark"></span>
    <span class="brand-name">Bluegate Lending Partners, Inc.</span>
  </div>

  <h1 class="headline">
    <span class="lead">HOME EQUITY</span>
    <span class="lead">LINES OF CREDIT</span>
    <span class="punch">ARE BACK!!!</span>
  </h1>
  <div class="head-rule"></div>

  <div class="ltv">
    <span class="ltv-figure">Up to 97.5%</span>
    <span class="ltv-note">On Owner Occupied<br>Properties</span>
  </div>

  <p class="tag tag-score">700 MINIMUM SCORES</p>
  <p class="tag tag-fund">FUND IN ONLY 2-3 WEEKS</p>

  <section class="uses">
    <h2>CAN BE USED FOR...</h2>
    <div class="uses-rule"></div>
    <ul>
      <li><svg width="14" height="14" viewBox="0 0 14 14"><circle cx="7" cy="7" r="7" fill="var(--gold)"/><path d="M3.8,7.2 L6,9.3 L10.2,4.9" fill="none" stroke="#fff" stroke-width="1.8"/></svg>Education Expense</li>
      <li><svg width="14" height="14" viewBox="0 0 14 14"><circle cx="7" cy="7" r="7" fill="var(--gold)"/><path d="M3.8,7.2 L6,9.3 L10.2,4.9" fill="none" stroke="#fff" stroke-width="1.8"/></svg>Bill Consolidation</li>
      <li><svg width="14" height="14" viewBox="0 0 14 14"><circle cx="7" cy="7" r="7" fill="var(--gold)"/><path d="M3.8,7.2 L6,9.3 L10.2,4.9" fill="none" stroke="#fff" stroke-width="1.8"/></svg>Investments</li>
      <li><svg width="14" height="14" viewBox="0 0 14 14"><circle cx="7" cy="7" r="7" fill="var(--gold)"/><path d="M3.8,7.2 L6,9.3 L10.2,4.9" fill="none" stroke="#fff" stroke-width="1.8"/></svg>Home Improvement</li>
    </ul>
  </section>

  <div class="phone">
    <svg width="42" height="42" viewBox="0 0 24 24" aria-hidden="true"><path fill="#fff" d="M6.6 10.8a15.2 15.2 0 0 0 6.6 6.6l2.2-2.2a1 1 0 0 1 1-.25 11.4 11.4 0 0 0 3.6.57 1 1 0 0 1 1 1V20a1 1 0 0 1-1 1A17 17 0 0 1 3 4a1 1 0 0 1 1-1h3.5a1 1 0 0 1 1 1c0 1.25.2 2.45.57 3.6a1 1 0 0 1-.25 1z"/><path d="M14.5 2.5a7 7 0 0 1 7 7M14.5 6a3.5 3.5 0 0 1 3.5 3.5" fill="none" stroke="#fff" stroke-width="1.6"/></svg>
    <span>(800) 417-2960</span>
  </div>

  <address class="contact">
    <p>Bluegate Lending Partners, Inc.</p>
    <p>NMLS #381760</p>
    <p class="web">www.bluegatelendhub.com</p>
  </address>
</main>
</body>
</html>
```